Mira Glow Opening Flyer (German Text Involved!)

We need a double-sided flyer design for a new beauty studio in Zurich, Switzerland called "Mira Glow" our services are Laser Hair Removal, Diode Laser, Manicure, Pedicure, Massage, Makeup, Facial, and Waxing. Our main service is Laser Hair Removal. We would like to see designs that use the colors purple and white. The final design should communicate beauty for men and women. You will find the Logo in the attachments.

The flyer must be 105mm wide x 210mm tall.

The following text must be on the flyer:

FRONT TEXT:
Unser “Mira Glow“ Studio liegt beim Haltestelle Lindenpark. Wir sind dein Partner für natürliche Schönheit, ob Haut, Nägel, Wimpern oder Haarentfernungen. Wir verschönern dein Aussehen mit professionellen Behandlungen.

Eröffnungsrabatt von 20% für Neukunden bis Ende November 2020 auf Diodenlaser-Behandlungen.

Wir freuen uns auf deinen Besuch.

Mira Glow, Lindenweg 27, 8047 Zürich, Tel. 044 382 17 49

www.mira-glow-studio.ch

BACK TEXT:
DIENSTLEISTUNGEN

Pediküre:
Auch Füsse brauchen Pflege. Die Pediküre mit erfrischendem Bad und kosmetischer Pflege zaubert Füsse, die sich sehen lassen können.

Maniküre:
Gepflegte Hände sind nicht nur unsere Visitenkarte, sie geben uns auch den ganzen Tag ein gutes Gefühl.

Haarentfernung:
Als attraktiv und ästhetisch gelten nicht nur eine gute Figur, sondern auch eine glatte, unbehaarte Haut, speziell für Frauen, aber zunehmend auch für Männer.

Wimpern-Lifting:
Voluminöse Wimpern geben den Augen Ausdrucksstärke und wirken verführerisch. Mit einem professionellen Wimpern-Lifting wird dieser Effekt noch verstärkt.

Maniküre, schon ab CHF 45.-
Pediküre, schon ab CHF 60.-
Dauerhafte Haarentfernung mit dem Diodenlaser, schon ab CHF 25.-
Haarentfernung mit Wachs, schon ab CHF 15.-

UNSERE ÖFFNUNGSZEITEN
Montag bis Samstag
09:00 bis 18:00

www.mira-glow-studio.ch

Target Market(s)

beauty for men and women

Industry/Entity Type

Beauty Salon

Colors
876aae

Requirements
Must have
• FRONT TEXT:

www.mira-glow-studio.ch

BACK TEXT:
DIENSTLEISTUNGEN

Pediküre:

Maniküre:

Haarentfernung:

Wimpern-Lifting:

UNSERE ÖFFNUNGSZEITEN
Montag bis Samstag
09:00 bis 18:00

www.mira-glow-studio.ch

```html
<!DOCTYPE html>
<html lang="de">
<head>
<meta charset="utf-8">
<title>Mira Glow Flyer</title>
<link href="https://fonts.googleapis.com/css2?family=Barlow:wght@400;700&family=Caveat:wght@500&display=swap" rel="stylesheet">
<style>
  :root {
    --stage: #00b8d4;
    --purple: #6a3f9a;
    --purple-dark: #5a3187;
    --white: #ffffff;
    --text-light: #f3ecfa;
  }
  * { box-sizing: border-box; margin: 0; padding: 0; }
  html, body { width: 1200px; height: 795px; overflow: hidden; }
  body { background: var(--stage); position: relative; font-family: "Barlow", sans-serif; }

  .flyer { position: absolute; width: 238px; height: 476px; background: var(--white); overflow: hidden; }
  .flyer-front { left: 338px; top: 149px; }
  .flyer-back { left: 620px; top: 152px; }
  .flyer-bg { position: absolute; inset: 0; width: 238px; height: 476px; }

  .brand { position: absolute; left: 0; right: 0; top: 34px; display: flex; align-items: center; justify-content: center; gap: 10px; }
  .brand-dot { width: 30px; height: 30px; border-radius: 50%; background: var(--purple); }
  .brand-name { font-family: "Barlow", sans-serif; font-weight: 400; font-size: 30px; color: var(--purple); letter-spacing: 0.5px; }

  .intro { position: absolute; left: 12px; right: 12px; top: 126px; text-align: center; font-family: "Caveat", cursive; font-weight: 500; color: var(--white); font-size: 17.5px; line-height: 18.5px; }
  .intro p + p { margin-top: 18.5px; }

  .contact { position: absolute; left: 0; right: 0; top: 396px; text-align: center; color: var(--purple); font-size: 9.5px; line-height: 12px; }
  .url { font-weight: 700; font-size: 9.5px; letter-spacing: 0.4px; color: var(--purple); text-align: center; position: absolute; left: 0; right: 0; }
  .flyer-front .url { top: 431px; }
  .flyer-back .url { top: 455px; }

  .back-title { position: absolute; left: 22px; top: 13px; font-weight: 700; font-size: 9.8px; color: var(--purple); letter-spacing: 0.2px; }
  .services { position: absolute; left: 22px; right: 20px; top: 48px; color: var(--text-light); font-size: 9.5px; line-height: 12.2px; }
  .service + .service { margin-top: 12.2px; }
  .service h3 { font-size: 9.5px; font-weight: 700; color: var(--white); }
  .prices { margin-top: 12.2px; }
  .prices b, .hours b { color: var(--white); }
  .hours { position: absolute; left: 22px; top: 392px; color: var(--text-light); font-size: 9.5px; line-height: 12.2px; }
  .hours h3 { font-size: 9.8px; font-weight: 700; color: var(--white); }
</style>
</head>
<body>

<section class="flyer flyer-front">
  <svg class="flyer-bg" viewBox="0 0 238 476" aria-hidden="true">
    <path fill="#6a3f9a" d="M0 101 C60 92 110 104 160 112 C200 118 225 110 238 103 L238 476 L0 476 Z"/>
    <path fill="#ffffff" d="M0 387 L10 384 L20 386 L34 383 L50 385 L70 382 L88 385 L110 383 L130 386 L150 382 L172 385 L194 383 L214 386 L238 383 L238 449 L224 452 L206 450 L186 453 L164 450 L140 452 L118 450 L96 453 L74 450 L52 452 L30 450 L12 452 L0 450 Z"/>
  </svg>
  <div class="brand">
    <span class="brand-dot"></span>
    <span class="brand-name">Mira Glow</span>
  </div>
  <div class="intro">
    <p>Unser “Mira Glow“ Studio liegt beim Haltestelle Lindenpark. Wir sind dein Partner für natürliche Schönheit, ob Haut, Nägel, Wimpern oder Haarentfernungen. Wir verschönern dein Aussehen mit professionellen Behandlungen.</p>
    <p>Eröffnungsrabatt von 20% für Neukunden bis Ende November 2020 auf Diodenlaser-Behandlungen.</p>
    <p>Wir freuen uns auf deinen Besuch.</p>
  </div>
  <p class="contact">Mira Glow, Lindenweg 27, 8047<br>Zürich, Tel. 044 382 17 49</p>
  <p class="url">WWW.MIRA-GLOW-STUDIO.CH</p>
</section>

<section class="flyer flyer-back">
  <svg class="flyer-bg" viewBox="0 0 238 476" aria-hidden="true">
    <path fill="#6a3f9a" d="M0 30 L14 32 L30 29 L48 31 L66 28 L86 31 L104 29 L124 32 L144 28 L164 31 L184 29 L204 32 L222 29 L238 31 L238 441 L222 443 L204 440 L184 443 L164 441 L144 444 L124 441 L104 443 L84 440 L64 443 L44 441 L24 444 L0 442 Z"/>
  </svg>
  <h2 class="back-title">DIENSTLEISTUNGEN</h2>
  <div class="services">
    <div class="service">
      <h3>Pediküre:</h3>
      <p>Auch Füsse brauchen Pflege. Die Pediküre mit erfrischendem Bad und kosmetischer Pflege zaubert Füsse, die sich sehen lassen können.</p>
    </div>
    <div class="service">
      <h3>Maniküre:</h3>
      <p>Gepflegte Hände sind nicht nur unsere Visitenkarte, sie geben uns auch den ganzen Tag ein gutes Gefühl.</p>
    </div>
    <div class="service">
      <h3>Haarentfernung:</h3>
      <p>Als attraktiv und ästhetisch gelten nicht nur eine gute Figur, sondern auch eine glatte, unbehaarte Haut, speziell für Frauen, aber zunehmend auch für Männer.</p>
    </div>
    <div class="service">
      <h3>Wimpern-Lifting:</h3>
      <p>Voluminöse Wimpern geben den Augen Ausdrucksstärke und wirken verführerisch. Mit einem professionellen Wimpern-Lifting wird dieser Effekt noch verstärkt.</p>
    </div>
    <p class="prices">
      Maniküre, schon ab <b>CHF 45.-</b><br>
      Pediküre, schon ab <b>CHF 60.-</b><br>
      Dauerhafte Haarentfernung mit dem<br>Diodenlaser, schon ab <b>CHF 25.-</b><br>
      Haarentfernung mit Wachs, schon ab <b>CHF 15.-</b>
    </p>
  </div>
  <div class="hours">
    <h3>UNSERE ÖFFNUNGSZEITEN</h3>
    <p>Montag bis Samstag</p>
    <p><b>09:00</b> bis <b>18:00</b></p>
  </div>
  <p class="url">WWW.MIRA-GLOW-STUDIO.CH</p>
</section>

</body>
</html>
```